資格は全部で2種類あります。
各々コースが2つに分かれており、それぞれ初級・中級・上級があります。
コース・級ごとに色合いを変えていただければと思っております。
※デザイン2種:各6色(2つのコース×3つの級)の色合い変更

今回はコンペ形式にて1種類のデザインを募集させていただきます。
採用させていただいた方には、2種類ともデザインしていただければと思っております。

また、認定証のデザインをもとにした、認定カードのデザインもお願いいたします。
※認定証同様、デザイン2種各6色の色合い変更

採用報酬は、認定証・認定カードのすべてのデザインを含めた金額になります。
今回のコンペでは、下記2点の認定証のデザインを募集させていただきます。
①「創造育成指導員」という資格の「発達障がい支援コース」の「初級」
②「デジタル匠指導員」という資格の「IT実践コース」の「初級」

記載いただきたい項目は下記の通りになります。

・初級
・認定証
・発達障がい支援アドバイザー
・●●殿
・●●年●月●日
・あなたは当カリキュラムを修了されましたので、『初級・発達障がい支援アドバイザー』として認定いたします。
・NPO法人青葉学習推進会

・初級
・認定証
・デジタル活用サポーター
・●●殿
・●●年●月●日
・あなたは当カリキュラムを修了されましたので、『初級・デジタル活用サポーター』として認定いたします。
・NPO法人青葉学習推進会
認定証はカミノハコにて発注予定となっているため、イラストレーターのデータにて納品いただきますようお願いいたします。
テンプレートにつきましては、下記ギガファイル便のデータをご確認ください。
https://files.examplestore-transfer.jp/1008-a71c2e9b40f35d8862e1c7a04b5f2913e

また、ロゴや認定証のサンプルを添付させていただきます。
イラストレーターのデータにつきましては下記ギガファイル便をご確認ください。
https://files.examplestore-transfer.jp/1005-3b8e0f41c92d7a65e0b1f4d82c6a07e15

ゴールドを差し色とした素敵なデザインであったので選ばせていただきました。
ありがとうございました。

この度は弊社のコンペにご参加いただきありがとうございました。
また機会がございましたら、よろしくお願いいたします。

```html
<!DOCTYPE html>
<html lang="ja">
<head>
<meta charset="UTF-8">
<title>認定証 初級 デジタル活用サポーター</title>
<link rel="stylesheet" href="https://fonts.googleapis.com/css2?family=Shippori+Mincho:wght@500;700;800&display=swap">
<style>
  :root {
    --paper-light: #fff7f9;
    --paper-pink: #f4cfdb;
    --frame-rose: #b24a6c;
    --frame-soft: #d88fa6;
    --title-mauve: #8a3451;
    --ink: #3b2a30;
    --badge-pink: #d9547f;
    --badge-deep: #b73764;
    --gold: #d8b46a;
    --org-brown: #8c2f34;
    --name-field: #ffffff;
  }
  * { margin: 0; padding: 0; box-sizing: border-box; }
  html, body { width: 846px; height: 1200px; overflow: hidden; }
  body { font-family: "Shippori Mincho", serif; color: var(--ink); }
  .certificate {
    position: relative; width: 846px; height: 1200px; overflow: hidden;
    background:
      radial-gradient(ellipse 70% 55% at 50% 48%, var(--paper-light) 0%, rgba(255,247,249,0.6) 55%, rgba(255,247,249,0) 100%),
      linear-gradient(160deg, #fbe6ec 0%, var(--paper-pink) 45%, #f8dce5 70%, var(--paper-pink) 100%);
  }
  .frame { position: absolute; inset: 0; }
  .flourish {
    position: absolute; width: 90px; height: 26px; border-radius: 13px;
    background: linear-gradient(90deg, rgba(178,74,108,0.15), rgba(178,74,108,0.45), rgba(178,74,108,0.15));
  }
  .flourish-left { left: 80px; top: 188px; }
  .flourish-right { right: 80px; top: 188px; }
  .title {
    position: absolute; left: 0; right: 0; top: 152px; text-align: center;
    font-size: 86px; font-weight: 800; letter-spacing: 26px; text-indent: 26px;
    color: var(--title-mauve); line-height: 1;
  }
  .subtitle {
    position: absolute; left: 0; right: 0; top: 278px; text-align: center;
    font-size: 21px; font-weight: 500; color: var(--title-mauve); letter-spacing: 1px;
  }
  .badge { position: absolute; left: 624px; top: 268px; width: 176px; height: 176px; }
  .badge-label {
    position: absolute; left: 0; right: 0; top: 64px; text-align: center;
    font-size: 48px; font-weight: 700; color: #fff; letter-spacing: 2px; line-height: 1.2;
  }
  .name-field {
    position: absolute; left: 163px; top: 480px; width: 514px; height: 156px;
    background: var(--name-field);
  }
  .honorific {
    position: absolute; left: 618px; top: 586px;
    font-size: 40px; font-weight: 700; color: var(--ink); line-height: 1;
  }
  .date {
    position: absolute; left: 0; right: 0; top: 684px; text-align: center;
    font-size: 26px; font-weight: 500; letter-spacing: 2px;
  }
  .date span { display: inline-block; width: 64px; }
  .divider {
    position: absolute; left: 308px; top: 756px; width: 230px; height: 24px;
    background: linear-gradient(90deg, rgba(178,74,108,0), rgba(178,74,108,0.5) 35%, rgba(178,74,108,0.5) 65%, rgba(178,74,108,0));
    border-radius: 12px;
  }
  .statement {
    position: absolute; left: 163px; top: 808px; width: 520px;
    font-size: 22px; font-weight: 500; line-height: 38px; letter-spacing: 0.5px;
  }
  .organisation {
    position: absolute; left: 0; right: 0; top: 1060px;
    display: flex; align-items: center; justify-content: center; gap: 14px;
    color: var(--org-brown); font-size: 30px; font-weight: 700; letter-spacing: 2px;
  }
  .organisation .mark { width: 26px; height: 26px; border-radius: 50%; background: var(--org-brown); }
</style>
</head>
<body>
<main class="certificate">
  <svg class="frame" width="846" height="1200" viewBox="0 0 846 1200" aria-hidden="true">
    <rect x="28" y="28" width="790" height="1144" fill="none" stroke="var(--frame-rose)" stroke-width="4"/>
    <rect x="40" y="40" width="766" height="1120" fill="none" stroke="var(--frame-soft)" stroke-width="1.5"/>
    <line x1="170" y1="136" x2="676" y2="136" stroke="var(--frame-rose)" stroke-width="2.5"/>
    <line x1="170" y1="142" x2="676" y2="142" stroke="var(--frame-rose)" stroke-width="1"/>
    <line x1="170" y1="266" x2="676" y2="266" stroke="var(--frame-rose)" stroke-width="1"/>
    <line x1="170" y1="318" x2="676" y2="318" stroke="var(--frame-rose)" stroke-width="1"/>
    <line x1="170" y1="324" x2="676" y2="324" stroke="var(--frame-rose)" stroke-width="2.5"/>
  </svg>

  <div class="flourish flourish-left" role="img" aria-label="左の飾り模様"></div>
  <div class="flourish flourish-right" role="img" aria-label="右の飾り模様"></div>
  <h1 class="title">認定証</h1>
  <p class="subtitle">デジタル活用サポーター</p>

  <div class="badge">
    <svg width="176" height="176" viewBox="0 0 176 176" aria-hidden="true">
      <defs>
        <radialGradient id="badgeFill" cx="45%" cy="40%" r="65%">
          <stop offset="0%" stop-color="#ee8aaa"/>
          <stop offset="60%" stop-color="var(--badge-pink)"/>
          <stop offset="100%" stop-color="var(--badge-deep)"/>
        </radialGradient>
      </defs>
      <circle cx="88" cy="92" r="80" fill="#fff"/>
      <circle cx="88" cy="92" r="74" fill="none" stroke="var(--gold)" stroke-width="3"/>
      <circle cx="88" cy="92" r="66" fill="url(#badgeFill)"/>
    </svg>
    <span class="badge-label">初級</span>
  </div>

  <div class="name-field" aria-label="氏名記入欄"></div>
  <span class="honorific">殿</span>

  <p class="date">令和<span></span>年<span></span>月<span></span>日</p>

  <div class="divider" role="img" aria-label="中央の飾り罫"></div>

  <p class="statement">あなたは当カリキュラムを修了されましたので、『初級・デジタル活用サポーター』として認定いたします。</p>

  <footer class="organisation">
    <span class="mark"></span>
    <span>NPO法人青葉学習推進会</span>
  </footer>
</main>
</body>
</html>
```